Nutrition data company website needs a new look

Our company is a B2B food database. We focus on nutrition and related health data like full nutrition profiles, product sourcing and packaging. Our goal is to provide the data that can help companies unleash their creativity to offer better foods and products.

Redesign our website to avoid food cliches. Every website that is interested in understanding health shows avocados, berries and salads. What can we do differently?

Take a look at our website

Plumtrel.ai

We like the look BUT we want to get away from typical food images. So…

Create the conceptual look for our website. What’s the visual hook? What’s a different visual style that could be interesting? Is it images of people that’s connected to food or data but not just typical stock photography? Is it an illustration style that brings everything to life? Is it more technical looking but still very human?

Be conceptual. Take some risks. We are open to very different ideas. It doesn’t mean you can’t use food. Just don’t look like every other health and nutrition site! Don’t just show typical stock photos.

WHAT WE LOVE ABOUT OUR CURRENT WEBSITE

It’s clean and simple. We like our logo and “blue” color. It human and not business or techy. You can use white space if you like, but don't have to.

WHAT WE DON’T LIKE

The use of food or people cliches

So the biggest asks are to avoid cliches and typical imagery. And don’t be too ‘visually busy’. We like a clean look. But surprise us!

Remember the customer is B2B but don’t be afraid to take any risks. Must look good on mobile too!
Updates

Need extra days to review

Hi. We will be making a decision shortly. Thank you all for all your hard work. You've all made this a difficult decision!

Target Market(s)

B2B customers, food manufacturers, food retailers, restaurants, food scientists etc

Industry/Entity Type

Data and food

Number of Pages Required

1 page

Font styles to use
Sans Serif
Other font styles liked:
• Montserrat, Proximanova but others too

Colors
0094D4
00A9DD
6FCCEA
C7EBF8
E9F6FB

Requirements
Must have
• Don't be cliche
Nice to have
• Simple clean look
Should not have
• Typical food or people stock imagery

```html
<!DOCTYPE html>
<html lang="en">
<head>
<meta charset="utf-8">
<title>Plumtrel — Truth in nutrition</title>
<link href="https://fonts.googleapis.com/css2?family=Montserrat:ital,wght@0,400;0,500;0,600;0,700;1,400&display=swap" rel="stylesheet">
<style>
:root{
  --blue:#1aabe2;
  --blue-deep:#0094d4;
  --blue-soft:#d8f1fa;
  --page:#f9fbfd;
  --ink:#0a1116;
  --navy:#03203a;
  --muted:#4a5560;
  --ring:#eef1f5;
}
*{margin:0;padding:0;box-sizing:border-box}
html,body{width:1200px;height:4164px;overflow:hidden}
body{background:var(--page);font-family:'Montserrat',sans-serif;color:var(--ink);position:relative}
.abs{position:absolute}
.hero{left:0;top:0;width:1200px;height:679px;border-radius:0 0 48px 48px;overflow:hidden;
  background:linear-gradient(180deg,#e4e4e4 0%,#dcdcdc 62%,#d2d4d6 70%,#e6e8ea 100%)}
.hero-photo{left:640px;top:0;width:560px;height:640px;
  background:radial-gradient(ellipse at 60% 55%,rgba(120,90,70,.35) 0%,rgba(220,220,220,0) 45%)}
.logo{left:74px;top:46px;font-size:30px;font-weight:700;color:#6e7378;letter-spacing:-.5px}
.nav{top:52px;font-size:15px;color:var(--ink)}
.nav.active{color:var(--blue)}
.hero-title{left:110px;top:166px;font-size:62px;font-weight:700;line-height:60px}
.hero-sub{left:110px;top:306px;font-size:23px}
.btn-blue{left:110px;top:364px;width:124px;height:50px;background:var(--blue);color:#fff;font-size:17px;display:flex;align-items:center;justify-content:center;border-radius:2px}
.bubble{border-radius:50%;background:#fff;display:flex;flex-direction:column;align-items:center;justify-content:center;box-shadow:0 2px 10px rgba(0,0,0,.08);line-height:1}
.bubble b{font-weight:500}
.bubble small{font-size:7px;letter-spacing:.5px;margin-top:2px}
.section-title{font-size:52px;font-weight:700;line-height:52px}
.how-text{left:611px;top:876px;width:480px;font-size:20px;line-height:30px}
.feature h3{font-size:40px;font-weight:500;line-height:44px}
.feature p{font-size:20px;line-height:30px;margin-top:6px;width:300px}
.photo{border-radius:50%;box-shadow:0 18px 36px rgba(0,40,80,.14)}
.power-text{left:108px;top:2818px;width:315px;font-size:13px;line-height:20px}
.power-text p+p{margin-top:20px}
.stat-big{left:875px;top:2688px;font-size:118px;font-weight:700;color:var(--blue);line-height:118px}
.stat-millions{left:877px;top:2822px;font-size:52px;font-weight:700;color:var(--blue)}
.stat-rev{left:877px;top:2882px;font-size:27px;color:var(--blue);letter-spacing:.5px}
.contact-band{left:0;top:3391px;width:1200px;height:495px;background:var(--blue);border-radius:48px}
.contact-title{left:108px;top:3490px;font-size:52px;font-weight:700;color:#fff;line-height:62px}
.field{left:592px;width:467px;border-bottom:2px solid #fff;color:rgba(255,255,255,.85);font-size:20px;font-style:italic;padding-bottom:4px}
.btn-white{left:592px;top:3714px;width:105px;height:44px;background:#fff;color:var(--ink);font-size:16px;display:flex;align-items:center;justify-content:center}
.hiring{left:108px;top:3976px;font-size:29px;font-weight:700}
.hiring-sub{left:108px;top:4014px;font-size:14px}
.btn-dark{left:108px;top:4057px;width:118px;height:33px;background:var(--navy);color:#fff;font-size:13px;display:flex;align-items:center;justify-content:center}
.foot-col{top:3978px;font-size:11px;line-height:24.5px;color:#2a3540}
.foot-col h4{font-size:11px;font-weight:700;letter-spacing:.5px;color:var(--ink);margin-bottom:4px}
</style>
</head>
<body>

<header class="abs hero" role="img" aria-label="Photo: hand pouring milk into a glass of iced coffee on a white textured tablecloth">
  <div class="abs hero-photo"></div>
</header>
<div class="abs logo">Plumtrel</div>
<nav>
  <span class="abs nav active" style="left:893px">Home</span>
  <span class="abs nav" style="left:977px">Careers</span>
  <span class="abs nav" style="left:1066px">Contact</span>
</nav>
<h1 class="abs hero-title">Truth in<br>nutrition</h1>
<p class="abs hero-sub">Food and beverage data insights</p>
<a class="abs btn-blue">Contact</a>

<div class="abs bubble" style="left:708px;top:331px;width:46px;height:46px;font-size:13px"><b>1.2g</b><small>PROTEIN</small></div>
<div class="abs bubble" style="left:910px;top:313px;width:88px;height:88px;font-size:20px"><b>50G</b><small style="font-size:9px">CARBS</small></div>
<div class="abs bubble" style="left:706px;top:422px;width:30px;height:30px;font-size:9px"><b>0.7g</b></div>
<div class="abs bubble" style="left:889px;top:462px;width:50px;height:50px;font-size:14px"><b>3.2g</b><small>FIBER</small></div>
<div class="abs bubble" style="left:694px;top:496px;width:94px;height:94px;font-size:28px"><b>89</b><small style="font-size:9px">CALORIES</small></div>

<section>
  <h2 class="abs section-title" style="left:110px;top:768px">How It</h2>
  <h2 class="abs section-title" style="left:213px;top:820px">Works?</h2>
  <p class="abs how-text">Simply put, food data is inaccurate, incomplete, and outdated. Plumtrel develops the data, insights, and tools that bring food and beverage information into the 21st century.</p>

  <div class="abs feature" style="left:192px;top:1276px"><h3>Science</h3><p>Pioneering research and discovery</p></div>
  <div class="abs photo" style="left:660px;top:1155px;width:346px;height:346px;background:radial-gradient(circle at 55% 45%,#e6eef4 0%,#9fb4c6 60%,#5d6f82 100%)" role="img" aria-label="Photo: gloved hand holding a petri dish in a lab"></div>

  <div class="abs photo" style="left:201px;top:1661px;width:346px;height:346px;background:radial-gradient(circle at 45% 60%,#e85a35 0%,#a9d3ef 38%,#8cc4ea 100%)" role="img" aria-label="Photo: red pot with noodles lifted into the air on blue background"></div>
  <div class="abs feature" style="left:689px;top:1783px"><h3>Industry</h3><p>Driving innovation and differentiation</p></div>

  <div class="abs feature" style="left:202px;top:2289px"><h3>Consumers</h3><p>Informing better choices and better health</p></div>
  <div class="abs photo" style="left:650px;top:2167px;width:346px;height:346px;background:radial-gradient(circle at 40% 50%,#6b5a52 0%,#b8c0c8 55%,#e3e7eb 100%)" role="img" aria-label="Photo: shopper reading a product label in a grocery aisle"></div>
</section>

<section>
  <h2 class="abs section-title" style="left:108px;top:2672px;line-height:56px">The power of<br>nutrition</h2>
  <div class="abs power-text">
    <p>Plumtrel is a data science company dedicated to advancing technology in a relentless pursuit of the most complete and transparent food and nutrition information.</p>
    <p>By developing transformational and frictionless solutions, our foundational goal is to inspire the world's creativity and unleash the greatness in every person and organization</p>
  </div>
  <svg class="abs" style="left:0;top:2800px" width="1200" height="420" viewBox="0 2800 1200 420">
    <circle cx="648" cy="3029" r="183" fill="var(--blue-soft)"/>
    <text x="647" y="3028" text-anchor="middle" font-family="Montserrat,sans-serif" font-weight="700" font-size="50" fill="var(--blue)">50+</text>
    <text x="645" y="3071" text-anchor="middle" font-family="Montserrat,sans-serif" font-size="24" fill="var(--blue)">Partnership</text>
    <polyline points="1003,2943 1003,3142 965,3142" fill="none" stroke="var(--blue)" stroke-width="1.2"/>
    <circle cx="839" cy="3090" r="129" fill="var(--ring)"/>
    <circle cx="839" cy="3090" r="110" fill="var(--blue)"/>
    <text x="839" y="3096" text-anchor="middle" font-family="Montserrat,sans-serif" font-weight="700" font-size="46" fill="#fff">20%</text>
    <text x="839" y="3130" text-anchor="middle" font-family="Montserrat,sans-serif" font-size="20" fill="#fff">Growth</text>
  </svg>
  <div class="abs stat-big">12+</div>
  <div class="abs stat-millions">Millions</div>
  <div class="abs stat-rev">REVENUES</div>
</section>

<section>
  <div class="abs contact-band"></div>
  <h2 class="abs contact-title">Work with,<br>partner with,<br>or join us</h2>
  <div class="abs field" style="top:3492px">Name</div>
  <div class="abs field" style="top:3558px">Email</div>
  <div class="abs field" style="top:3623px">Type messege here....</div>
  <a class="abs btn-white">Submit</a>
</section>

<footer>
  <h3 class="abs hiring">We’re hiring!</h3>
  <p class="abs hiring-sub">Lorem ipsum dolor sit amet</p>
  <a class="abs btn-dark">Learn more</a>
  <div class="abs foot-col" style="left:453px"><h4>PRODUCT</h4>How it works<br>Features<br>Pricing<br>Testimonials</div>
  <div class="abs foot-col" style="left:619px"><h4>ABOUT</h4>Our team<br>Careers<br>Press<br>Stores</div>
  <div class="abs foot-col" style="left:786px"><h4>CONNECT</h4>Friendbook<br>Chirper<br>Snapgram<br>Linkwork</div>
  <div class="abs foot-col" style="left:952px"><h4>CONTACT</h4>hello@plumtrel.ai<br>555-014-2290<br>418 Linden Bay Suite 204</div>
</footer>

</body>
</html>
```